Zelphone/Zelpad App Developer Showcase Website (Redesign)

We need an attractive, modern and professional looking re-design of an existing website: www.velkrimo.com.

We have a new logo and want the website to use this - although the colors used in the logo could be altered to suit the website color scheme.

This site should consist of
- a main page showing off a few sample of apps
- a separate page for each app (one page template suitable for all apps)
- a few subsidiary pages which can be based on a single similar template, such as an About page, and Help pages for some of the apps

Note - some of the apps are Zelphone only, and others are Zelpad only or for both. Hence the design should allow for showing off both.

There is no need for the design to allow for lots of app screenshots (there will be links to the wareshelf where more screenshot can be seen).

It is not necessary to optimise the design just for Zelphone screen viewing, but the
website should at least be reasonably usable on an Zelphone and Zelpad, as many users may be accessing the site from those devices.

Here are a few sites of similar developers - just for ideas. The first one listed is the one I think is the most attractive design. The main difference needed is that the primary function of this site is to show off the quality of the apps to app buyers, rather than to promote ourselves as app developers, which is only a secondary aim.

http://www.trelbworks.com.au/mobilebuilds.html
http://www.quendix.com.au/
http://www.parvolent.com/

Note - app screenshots and Zelphone and Zelpad device graphics templates (including glassy shadowed versions) are attached in a zip file.

Thank-you for all your submissions - your efforts are much appreciated. :-)

Seeing all the proposed designs has allowed me to see where I perhaps haven't been very clear in my brief, and also has helped me work out what type of design elements I prefer. So following is a refinement of the requirement.

The site requires only a simple layout ie.
At most it needs
- A Home page showing off a few screenshots, or with a scrolling/dynamic element, and a single link to veLKRM in the wareshelf
- An About Us page
- A Contact Us page (with email form for two types are enquires a) App Support Enquiry b) Business Enquiry
- A Page for each app, including 
  > some phone/screenshot graphics
  > a description of the app features
  > a link to buy the app in the wareshelf
  > a Viewtrove video demo link (for some apps only)
  > a link to a Help/FAQ page (for some apps only)

Note - if your design can show all the app info within the main page (eg. in a scrolling frame of some kind), then separate pages for each app might not even be required.

Things that are not needed are
- Request a Quote
- Follow us via Chatterleaf, Blipwire etc...

Regarding the graphical design elements, I have decided that I do prefer
- designs with lighter colored backgrounds, so not black or very dark designs
- designs that keep the orange/black colors in the velkrimo logo, and use colors which work well with these

I will now contact some of you individually with specific feedback where I can - but there are so many designs already that I may not be able to contact everyone. If not, please do review your design in light of the above comments to see how well it fits.

Thanks again, and I am very pleased with results so far!

Target Market(s)

1. Zelphone/Zelpad owners looking for useful apps - tech savvy, well-educated
2. Companies/people looking for experienced/expert ZOS development company

Requirements
Must have
• Expandable to allow new page to be added for each future apps

Use the attached new company logo design (although colors may be altered to suit website color scheme)

Site must be maintainable/expandable by ourselves once initial site is in place.
Nice to have
• Website nicely viewable from Zelphone browser

Would be nice to have some dynamic elements eg. scrolling showcase of different app screens on main page

```html
<!DOCTYPE html>
<html lang="en">
<head>
<meta charset="utf-8">
<title>velkrimo – Apps</title>
<link href="https://fonts.googleapis.com/css2?family=Source+Sans+3:wght@400;600&display=swap" rel="stylesheet">
<style>
:root{
  --band-green:#cddfbf;
  --band-green-dark:#bccfae;
  --nav-line:#a9bf98;
  --panel:#fafafa;
  --page:#ffffff;
  --text-dark:#4a4f4a;
  --text-mid:#666;
  --text-soft:#aaa;
  --ribbon-top:#92d9f1;
  --ribbon-bottom:#6ac6e8;
  --logo-orange:#f29a12;
}
*{margin:0;padding:0;box-sizing:border-box}
html,body{width:1200px;height:850px;overflow:hidden}
body{position:relative;background:var(--page);font-family:"Source Sans 3",Arial,sans-serif;color:var(--text-dark)}
.header{position:absolute;left:0;top:0;width:1200px;height:108px;background:linear-gradient(var(--band-green) 0,var(--band-green) 60px,var(--band-green-dark) 75px)}
.nav-bar{position:absolute;left:0;top:75px;width:1200px;height:33px;background:linear-gradient(#cfe1c1,#c3d8b3);border-top:1px solid var(--nav-line)}
.nav-link{position:absolute;top:78px;font-size:21px;color:var(--text-dark);text-decoration:none;line-height:30px}
.nav-sep{position:absolute;top:82px;width:1px;height:24px;background:#9fb38f}
.nav-marker{position:absolute;left:376px;top:75px;width:0;height:0;border-left:8px solid transparent;border-right:8px solid transparent;border-top:8px solid var(--nav-line)}
.logo-box{position:absolute;left:499px;top:0;width:184px;height:100px;background:#fff;border-radius:0 0 10px 10px;box-shadow:0 3px 8px rgba(0,0,0,.15);display:flex;align-items:center;justify-content:center}
.logo-name{font-size:34px;font-weight:600;color:var(--logo-orange);letter-spacing:-.5px}
.panel{position:absolute;left:96px;top:108px;width:1001px;height:662px;background:var(--panel)}
.crumbs{position:absolute;left:193px;top:128px;font-size:15px;color:var(--text-mid);display:flex;align-items:center;gap:6px}
.crumbs .sep{margin:0 8px 0 4px}
.ribbon{position:absolute;left:193px;top:197px}
.ribbon span{position:absolute;left:29px;top:0;line-height:34px;color:#fff;font-size:25px}
.section-title{position:absolute;left:195px;font-size:21px;color:var(--text-soft);display:flex;align-items:center;gap:8px}
.app{position:absolute;width:90px;text-align:center;font-size:11px;color:var(--text-mid)}
.app .icon{display:block;width:52px;height:52px;margin:0 auto 7px;border-radius:9px;box-shadow:0 1px 2px rgba(0,0,0,.25)}
.footer{position:absolute;left:0;top:770px;width:1200px;height:80px;background:linear-gradient(var(--band-green) 0,var(--band-green) 55px,#b9cca9 80px);text-align:center;font-size:16px;line-height:90px;color:var(--text-dark)}
.i-sun{background:radial-gradient(circle at 50% 45%,#ffd84a,#e28a14 45%,#3b2a10 85%)}
.i-wind{background:radial-gradient(circle,#3fc7d6 10%,#2a3a3e 60%,#1c1f20)}
.i-seek{background:radial-gradient(circle at 50% 40%,#ffe07a,#f07b1c 40%,#7a3f7a 90%)}
.i-moon{background:radial-gradient(circle at 50% 40%,#5fe7ff,#2a7fd8 40%,#8a3e75 90%)}
.i-eye{background:radial-gradient(circle,#6f8aa0 20%,#c9a13b 55%,#7a5a1e)}
.i-calm{background:linear-gradient(#f6d6a8,#f0a86b 50%,#6f6a70)}
</style>
</head>
<body>
<header class="header"></header>
<nav class="nav-bar"></nav>
<span class="nav-marker"></span>
<a class="nav-link" style="left:193px">Home</a>
<span class="nav-sep" style="left:305px"></span>
<a class="nav-link" style="left:363px">Apps</a>
<a class="nav-link" style="left:762px">About us</a>
<span class="nav-sep" style="left:909px"></span>
<a class="nav-link" style="left:960px">Contact us</a>
<div class="logo-box"><span class="logo-name">velkrimo</span></div>

<main class="panel"></main>

<div class="crumbs">
  <svg width="15" height="15" viewBox="0 0 15 15"><path d="M7.5 1 L14 7 H12 V14 H9 V10 H6 V14 H3 V7 H1 Z" fill="#777"/></svg>
  <span>Home</span>
  <svg class="sep" width="8" height="12" viewBox="0 0 8 12"><path d="M1 1 L6 6 L1 11" stroke="#777" stroke-width="1.5" fill="none"/></svg>
  <span>Apps</span>
</div>

<div class="ribbon">
  <svg width="130" height="37" viewBox="0 0 130 37">
    <defs><linearGradient id="rib" x1="0" y1="0" x2="0" y2="1"><stop offset="0" stop-color="var(--ribbon-top)"/><stop offset="1" stop-color="var(--ribbon-bottom)"/></linearGradient></defs>
    <path d="M0 0 H116 L129 18.5 L116 37 H0 Z" fill="url(#rib)"/>
  </svg>
  <span>Apps</span>
</div>

<h2 class="section-title" style="top:281px">
  <svg width="18" height="31" viewBox="0 0 18 31"><rect x="1" y="1" width="16" height="29" rx="3" fill="none" stroke="#bbb" stroke-width="2"/><rect x="4" y="5" width="10" height="19" fill="#ddd"/><circle cx="9" cy="27" r="1.3" fill="#bbb"/></svg>
  Zelphone apps
</h2>
<div class="app" style="left:173px;top:334px"><span class="icon i-sun" role="img" aria-label="Roo Skies app icon, golden sun"></span>Roo Skies</div>
<div class="app" style="left:261px;top:334px"><span class="icon i-wind" role="img" aria-label="Tide Drift app icon, turbine dial"></span>Tide Drift</div>
<div class="app" style="left:354px;top:334px"><span class="icon i-seek" role="img" aria-label="Sol Tracker app icon, sun over horizon"></span>Sol Tracker</div>
<div class="app" style="left:451px;top:334px"><span class="icon i-moon" role="img" aria-label="Luna Tracker app icon, glowing moon"></span>Luna Tracker</div>
<div class="app" style="left:547px;top:334px"><span class="icon i-eye" role="img" aria-label="Clima Lens app icon, globe in gold frame"></span>Clima Lens</div>
<div class="app" style="left:646px;top:335px"><span class="icon i-calm" role="img" aria-label="Calm &amp; Resolve app icon, sunset over sea"></span>Calm &amp; Resolve</div>

<h2 class="section-title" style="top:477px">
  <svg width="24" height="31" viewBox="0 0 24 31"><rect x="1" y="1" width="22" height="29" rx="2" fill="none" stroke="#bbb" stroke-width="2"/><rect x="4" y="4" width="16" height="22" fill="#ddd"/></svg>
  Zelpad apps
</h2>
<div class="app" style="left:174px;top:532px"><span class="icon i-sun" role="img" aria-label="Roo Skies HD app icon, golden sun"></span>Roo Skies HD</div>
<div class="app" style="left:263px;top:532px"><span class="icon i-wind" role="img" aria-label="Tide Drift app icon, turbine dial"></span>Tide Drift</div>
<div class="app" style="left:355px;top:531px"><span class="icon i-seek" role="img" aria-label="Sol Tracker app icon, sun over horizon"></span>Sol Tracker</div>

<footer class="footer">©&nbsp; 2011 Brenvale Pty Ltd</footer>
</body>
</html>
```